Warehouse Surplus Flyer

2 Sided Flyer to be used in print and online for short, unadvertised sale to pharmacies for prescription vials. Please feel free to edit wordiness.

Side One:
WE PASS ALONG THE SAVINGS TO YOU
WAREHOUSE SURPLUS UNADVERTISED OFFER
BY INVITATION ONLY TO YOU

We have a acquired a surplus, with our supplier, on ALL AMBER color and ALL with CHILD RESISTANT CAPS and we would like to pass along the savings to you, as we need to make room for other inventory.

Normally these vials sell for over $50 a case! We are going to move these vials at very special pricing.

Very cost-effective, Quality Vials

KTR Supply provides pharmacy vials in the independent pharmacy market and conditioned toner cartridges in pharmacies and several other vertical markets.
Please call us at 888-412-5096 and we will be happy to work with you directly.

ktrsupplyco.com

This is not an advertised sale. Offer Ends September 30, 2013*.

2nd Side:
VIAL SIZE QUANTITY PER CASE CASES AVAILABLE
8 Dram 410 50
10 Dram 360 50
13 Dram 310 500
16 Dram 260 500
20 Dram 270 500
30 Dram 240 500
40 Dram 200 500
60 Dram 140 100

During this offer to move inventory, we are selling these at 30% to 50% off our already discounted rate, based on volume.

Quantities: (*While Supplies Last)
• 1 to 500 cases will be sold at 30% off our discounted price! $28 Per Case
• 501 to 1000 cases will be sold at 40% our discounted price! $25 Per Case
• Over 1000 cases will be sold at 50% our discounted price! $22 Per Case

We also have great pricing on conditioned toner cartridges. You can also view our line of products and prices on www.ktrsupplyco.com.

Please call us at 888-412-5096 and we will be happy to work with you directly. This is not an advertised sale.
Updates

Deadline IS AUGUST 28TH! SEPTEMBER SALE.

Target Market(s)

Independent Pharmacies

Industry/Entity Type

Online

Requirements
Must have
• 3 color or Less front side, 2 Sided Flyer
• Backside can be 1 Color
• Phone Number
• web address
• sales expiration date
Nice to have
• graphic call outs to gain attention

```html
<!DOCTYPE html>
<html lang="en">
<head>
<meta charset="utf-8">
<title>Warehouse Surplus Flyer – Vial Pricing</title>
<link href="https://fonts.googleapis.com/css2?family=Archivo+Black&family=Arimo:wght@400;700&display=swap" rel="stylesheet">
<style>
  :root {
    --paper: #ffffff;
    --ink: #111111;
    --row-dark: #d3d3d3;
    --row-light: #efefef;
    --offer-blue: #3056e0;
    --link-blue: #2a3fb0;
    --sale-red: #ee1c1c;
    --badge-gray: #555555;
  }
  html, body {
    margin: 0;
    padding: 0;
    width: 927px;
    height: 1200px;
    overflow: hidden;
    background: var(--paper);
  }
  .flyer {
    position: relative;
    width: 927px;
    height: 1200px;
    overflow: hidden;
    background: var(--paper);
    font-family: "Arimo", Arial, sans-serif;
    color: var(--ink);
  }
  .spectrum-band {
    position: absolute;
    left: 14px; top: 0;
    width: 104px; height: 1200px;
    background: linear-gradient(90deg, #9be23a 0%, #f3e92e 18%, #ff9a1f 32%, #ff2a2a 46%, #e0208c 58%, #7a2ad8 70%, #2f56e8 82%, #19c3e8 100%);
  }
  .spokesperson {
    position: absolute;
    left: 88px; top: 182px;
    width: 208px; height: 592px;
    background: linear-gradient(180deg, #d9b79a 0%, #2c2c2c 12%, #1d1d1d 80%, #8a5a34 100%);
    border-radius: 60px 60px 12px 12px;
    opacity: .9;
  }
  .headline {
    position: absolute;
    left: 153px; top: 30px;
    margin: 0;
    font-family: "Archivo Black", "Arial Black", sans-serif;
    font-size: 36px;
    line-height: 44px;
    letter-spacing: 1.5px;
    text-transform: uppercase;
  }
  .stock-table {
    position: absolute;
    left: 292px; top: 201px;
    width: 635px;
  }
  .stock-row {
    height: 46px;
    margin-bottom: 2.4px;
    padding-left: 31px;
    font-size: 27px;
    line-height: 46px;
    font-weight: 400;
    -webkit-text-stroke: .4px var(--ink);
    background: var(--row-dark);
    white-space: pre;
  }
  .stock-row:nth-child(even) { background: var(--row-light); }
  .bubble-trail {
    position: absolute;
    left: 589px; top: 246px;
    width: 338px; height: 306px;
    background: radial-gradient(ellipse at 45% 45%, rgba(20,20,20,.35), rgba(20,20,20,0) 70%);
  }
  .offer-note {
    position: absolute;
    left: 325px; top: 607px;
    margin: 0;
    width: 560px;
    color: var(--offer-blue);
    font-weight: 700;
    font-size: 27.5px;
    line-height: 34.5px;
  }
  .discount-badge {
    position: absolute;
    left: 14px;
    width: 112px; height: 112px;
    border-radius: 50%;
    background: var(--paper);
    text-align: center;
    font-weight: 700;
  }
  .badge-30 { top: 812px; color: var(--sale-red); font-size: 46px; line-height: 112px; }
  .badge-to { top: 921px; color: var(--badge-gray); font-size: 46px; line-height: 104px; }
  .badge-50 { top: 1030px; color: var(--sale-red); font-size: 46px; line-height: 46px; padding-top: 20px; height: 92px; }
  .badge-50 span { display: block; font-size: 30px; line-height: 28px; }
  .pricing {
    position: absolute;
    left: 175px; top: 815px;
    width: 740px;
  }
  .pricing h2 {
    margin: 0 0 26px;
    font-size: 26px;
    line-height: 34px;
    font-weight: 700;
  }
  .tiers {
    margin: 0 0 22px;
    padding: 0;
    list-style: none;
    font-size: 18.6px;
    line-height: 23.5px;
    font-weight: 700;
  }
  .tiers li::before { content: "\2022\00a0"; }
  .pricing p {
    margin: 0 0 22px;
    font-size: 18.6px;
    line-height: 23.5px;
    font-weight: 700;
  }
  .web-link { color: var(--link-blue); text-decoration: none; }
</style>
</head>
<body>
<div class="flyer">
  <div class="spectrum-band" role="img" aria-label="Vertical band of rainbow-coloured stripes"></div>

  <h1 class="headline">Vial Size Quantity<br>Per Case Cases Available</h1>

  <div class="spokesperson" role="img" aria-label="Illustration of a smiling salesman in a dark suit"></div>

  <div class="stock-table">
    <div class="stock-row">08 Dram 410    50</div>
    <div class="stock-row">10 Dram 360    50</div>
    <div class="stock-row">13 Dram 310  500</div>
    <div class="stock-row">16 Dram 260 500</div>
    <div class="stock-row">20 Dram 270 500</div>
    <div class="stock-row">30 Dram 240 500</div>
    <div class="stock-row">40 Dram 200 500</div>
    <div class="stock-row">60 Dram 140 100</div>
  </div>

  <div class="bubble-trail" role="img" aria-label="Decorative trail of black and glossy bubbles rising from a shadow"></div>

  <p class="offer-note">During this offer to move inventory, we are selling these at 30% to 50% off our already discounted rate, based on volume.</p>

  <div class="discount-badge badge-30">30%</div>
  <div class="discount-badge badge-to">to</div>
  <div class="discount-badge badge-50">50%<span>off</span></div>

  <section class="pricing">
    <h2>Quantities: (*While Supplies Last)</h2>
    <ul class="tiers">
      <li>1 to 500 cases will be sold at 30% off our discounted price! $28 Per Case</li>
      <li>501 to 1000 cases will be sold at 40% our discounted price! $25 Per Case</li>
      <li>Over 1000 cases will be sold at 50% our discounted price! $22 Per Case</li>
    </ul>
    <p>We also have great pricing on conditioned toner cartridges.<br>You can also view our line of products and prices<br>on <a class="web-link" href="#">www.ktrsupplyco.com.</a></p>
    <p>Please call us at&nbsp; 888-412-5096&nbsp; and we will be happy to work with you<br>directly. This is not an advertised sale.</p>
  </section>
</div>
</body>
</html>
```